Poster Design - Stand Up Paddle Eco Tour

We need a A3 size poster design (using Adobe Illustrator) for our company's stand up paddle tour. Our tour is on flat water, calm and safe, suitable for all ages and level.

WE provide worldclass SUP boards for our customers. And branded Tovar Helsby life jacket. Our instructors are all well trained and exeprience. Plus they are super friendly. Every paddling trip come with a safety boat.

Please refer to attached files for text and photos.

Our website is www.brimwakeglide.com.sg

IMPORTANT NOTE - The design has to be done in Adobe Illustrator. The winning designer has to submit the working file in Adobe Illustrator.

Target Market(s)

Working adult - 20 - 35 year old

Industry/Entity Type

Tourism

Requirements
Must have
• The project MUST be done in Adobe Illustrator and the winning designer has to submit the artwork to us in Adobe Illustrator format.
Nice to have
• pleasant to look at.

```html
<!DOCTYPE html>
<html lang="en">
<head>
<meta charset="utf-8">
<title>Brimwake Glide – SUP Eco Tour Poster</title>
<link rel="stylesheet" href="https://fonts.googleapis.com/css2?family=Oswald:wght@500&family=Open+Sans:ital,wght@0,400;0,700;1,700&display=swap">
<style>
  :root {
    --navy: #1b2a3a;
    --slate: #4a4f5c;
    --paper: #dcdddf;
    --paper-dark: #c3c5c8;
    --ink: #1e2631;
    --ink-soft: #2f3a47;
    --white: #ffffff;
    --frame: #a9acb0;
  }
  * { box-sizing: border-box; margin: 0; padding: 0; }
  html, body { width: 872px; height: 1200px; overflow: hidden; }
  body { background: var(--paper); font-family: "Open Sans", Arial, sans-serif; color: var(--ink); }

  .poster { position: relative; width: 872px; height: 1200px; overflow: hidden; background: linear-gradient(180deg, #e4e5e6 0%, var(--paper) 100%); }

  .hero { position: absolute; left: 0; top: 0; width: 872px; height: 591px; }
  .hero-photo { position: absolute; inset: 0;
    background: linear-gradient(180deg, #b9cbe0 0%, #d8e2ea 22%, #3f5a36 38%, #2f4a2c 52%, #6b6e4a 64%, #5b6042 100%); }
  .hero-shapes { position: absolute; inset: 0; }

  .headline { position: absolute; left: 34px; top: 30px; width: 520px;
    font-family: "Oswald", "Arial Narrow", sans-serif; font-weight: 500; font-size: 29px;
    line-height: 36px; color: var(--white); text-transform: uppercase; letter-spacing: 0.2px; }

  .tour-facts { position: absolute; right: 22px; top: 476px; text-align: right;
    font-size: 11px; line-height: 14px; color: var(--white); }
  .tour-facts dt { text-transform: uppercase; }
  .tour-facts dd { margin-bottom: 10px; }

  .guided { position: absolute; left: 34px; top: 622px; width: 820px; }
  .guided h2 { font-size: 15px; font-weight: 700; text-transform: uppercase; color: var(--ink); }
  .guided p { font-size: 14.5px; line-height: 20px; margin-top: 3px; color: var(--ink); }

  .gallery { position: absolute; top: 723px; left: 0; width: 872px; height: 176px; }
  .gallery-item { position: absolute; top: 0; width: 242px; height: 176px; border: 3px solid var(--frame); }
  .gallery-item.open-water { left: 52px; background: linear-gradient(180deg, #a9c3e0 0%, #dfe7ef 35%, #8a9aa0 55%, #9ba7a4 100%); }
  .gallery-item.mangrove { left: 315px; background: linear-gradient(180deg, #dbe6ef 0%, #3d5d37 25%, #3b5734 50%, #7f8a78 70%, #8c968a 100%); }
  .gallery-item.group { left: 583px; background: linear-gradient(180deg, #7fa6d6 0%, #cfdcea 45%, #8b99a0 62%, #9aa6a6 100%); }

  .corner-band { position: absolute; left: 0; top: 0; width: 872px; height: 1200px; pointer-events: none; }

  .brand { position: absolute; left: 31px; top: 1010px; display: flex; align-items: center; gap: 8px;
    font-size: 20px; font-weight: 700; color: var(--navy); }
  .brand-dot { width: 14px; height: 14px; border-radius: 50%; background: var(--navy); }

  .promise { position: absolute; left: 235px; top: 1000px; font-size: 14.5px; line-height: 21px; color: var(--ink-soft); }
  .promise .call { font-style: italic; font-weight: 700; font-size: 16px; color: var(--ink); }

  .contact { position: absolute; right: 21px; top: 1087px; text-align: right; font-size: 14.5px; line-height: 23px; color: var(--white); }
  .contact .web { font-weight: 700; }

  .booking-strip { position: absolute; left: 0; top: 1153px; height: 47px; width: 560px;
    background: var(--paper-dark); padding: 13px 0 0 28px; font-size: 15.5px; color: var(--ink-soft); }
  .booking-strip strong { font-weight: 700; color: var(--ink); }
</style>
</head>
<body>
<main class="poster">
  <section class="hero">
    <div class="hero-photo" role="img" aria-label="Group of paddlers on stand up paddle boards raising their paddles on a calm mangrove river"></div>
    <svg class="hero-shapes" width="872" height="591" viewBox="0 0 872 591" aria-hidden="true">
      <polygon points="0,0 520,0 0,362" fill="#3a3f4c" fill-opacity="0.82"/>
      <polygon points="520,0 760,0 0,530 0,362" fill="#3a3f4c" fill-opacity="0.28"/>
      <polygon points="872,322 872,591 545,591" fill="#1e2530" fill-opacity="0.55"/>
    </svg>
    <h1 class="headline">Explore the natural coastal surroundings and waterways of Johor on a SUP adventure touring board</h1>
    <dl class="tour-facts">
      <dt>Timing:</dt>
      <dd>Morning, afternoon, and sunset session</dd>
      <dt>Location:</dt>
      <dd>Sela Rinda River, set off from Teluk Marani,<br>Pasir Lendang. (next to Pasir Seroja)</dd>
    </dl>
  </section>

  <section class="guided">
    <h2>What could be better than a group guided tour?</h2>
    <p>With life vests and a safety boat for our guided tour, you can be assured of a secured environment while you focus on just having fun and creating life's best memories with friends and family.</p>
  </section>

  <div class="gallery">
    <div class="gallery-item open-water" role="img" aria-label="Paddlers standing on boards on open coastal water"></div>
    <div class="gallery-item mangrove" role="img" aria-label="Two paddlers on yellow boards beside a mangrove shore"></div>
    <div class="gallery-item group" role="img" aria-label="Large group of paddle boarders gathered on the water"></div>
  </div>

  <svg class="corner-band" width="872" height="1200" viewBox="0 0 872 1200" aria-hidden="true">
    <polygon points="872,915 872,1200 472,1200" fill="var(--navy)"/>
  </svg>

  <div class="brand"><span class="brand-dot"></span>Brimwake Glide</div>

  <section class="promise">
    <p>Our tours are flat-water and appropriate for all ages and levels.</p>
    <p>We have the best possible service and equipment.</p>
    <p class="call">Join us for a fun and relaxing day.</p>
  </section>

  <address class="contact" style="font-style:normal">
    Contact us for booking.<br>
    We do not accept walk-in.<br>
    <span class="web">www.brimwakeglide.com.sg</span><br>
    Social: Brimwake Glide
  </address>

  <div class="booking-strip">Booking Contact: <strong>booking@brimwakeglide.com.sg</strong></div>
</main>
</body>
</html>
```